velvet trinket crate

My business is an adult toy and lingerie store. I need a catalogue listing multiple products on one page along with descriptions and prices. They must be two sided and in color. I can provide a sample to illustrate my request. I have hundreds of products . This is an actual hard copy catalogue I'm asking for.
Updates
I just uploaded a excel file . please tell if you are able to use/ open this file;.
Target Market(s)
Adults only
Industry/Entity Type
Adult
Look and feel
Each slider illustrates characteristics of the customer's brand and the style your logo design should communicate.

```html
<!DOCTYPE html>
<html lang="en">
<head>
<meta charset="utf-8">
<title>velvet trinket crate — Catalogue Spread</title>
<link href="https://fonts.googleapis.com/css2?family=Open+Sans:wght@400;600;700&family=Ubuntu:wght@500;700&display=swap" rel="stylesheet">
<style>
  :root {
    --backdrop: #3b2b23;
    --page-dark: #4e0a12;
    --page-mid: #6e121d;
    --page-light: #86202b;
    --ribbon: #c3142c;
    --ribbon-dark: #8d0c1e;
    --ink: #ffffff;
    --ink-soft: #f1d6d8;
    --strip: #120406;
    --frame: #ffffff;
    --divider: rgba(255, 255, 255, 0.35);
  }
  * { box-sizing: border-box; margin: 0; padding: 0; }
  html, body {
    width: 1200px; height: 1037px; overflow: hidden;
    background: var(--backdrop);
    font-family: "Open Sans", sans-serif;
    color: var(--ink);
  }
  .spread {
    position: absolute; left: 20px; top: 68px;
    width: 1160px; height: 900px;
    display: flex;
    box-shadow: 0 10px 30px rgba(0,0,0,0.5);
  }
  .page {
    position: relative; width: 580px; height: 900px;
    background: radial-gradient(ellipse at 50% 45%, var(--page-light), var(--page-mid) 55%, var(--page-dark));
    overflow: hidden;
  }
  .page--left { box-shadow: inset -18px 0 24px -16px rgba(0,0,0,0.6); }
  .page--right { box-shadow: inset 18px 0 24px -16px rgba(0,0,0,0.6); }
  .page__stripe {
    position: absolute; left: 0; right: 0; top: 56px; height: 10px;
    background: var(--ribbon);
  }
  .page__stripe::after {
    content: ""; position: absolute; left: 0; right: 0; top: 14px; height: 2px;
    background: var(--ribbon-dark);
  }
  .brand {
    position: absolute; top: 14px; width: 86px; height: 86px;
    background: var(--frame); border-radius: 6px;
    display: flex; align-items: center; justify-content: center; text-align: center;
    font-family: "Open Sans", sans-serif; font-weight: 700; font-size: 13px; line-height: 1.15;
    color: var(--ribbon);
    box-shadow: 0 3px 8px rgba(0,0,0,0.45);
    z-index: 2;
  }
  .page--left .brand { left: 168px; }
  .page--right .brand { left: 200px; }

  .catalogue-grid {
    position: absolute; left: 20px; right: 20px; top: 110px; height: 730px;
    display: grid; grid-template-columns: 1fr 1fr; grid-template-rows: repeat(3, 1fr);
  }
  .product {
    position: relative; padding: 10px 10px 6px;
    border-bottom: 1px dashed var(--divider);
    overflow: hidden;
  }
  .product:nth-child(odd) { border-right: 1px dashed var(--divider); }
  .product:nth-child(n+5) { border-bottom: none; }

  .ribbon {
    display: inline-block;
    font-family: "Ubuntu", sans-serif; font-weight: 500; font-size: 15px; line-height: 1.05;
    background: var(--ribbon); color: var(--ink);
    padding: 5px 18px 5px 12px;
    clip-path: polygon(0 0, 100% 0, 94% 100%, 0 100%);
    box-shadow: 0 2px 4px rgba(0,0,0,0.4);
    max-width: 230px;
  }
  .product:nth-child(even) .ribbon { clip-path: polygon(6% 0, 100% 0, 100% 100%, 0 100%); padding: 5px 12px 5px 18px; }
  .lead {
    display: flex; gap: 6px; align-items: flex-start;
    font-size: 9px; line-height: 1.3; margin: 7px 0 6px; color: var(--ink-soft);
  }
  .lead::before {
    content: ""; flex: none; width: 9px; height: 9px; margin-top: 1px;
    background: var(--ribbon);
  }
  .body { display: flex; gap: 10px; }
  .photo-wrap { position: relative; flex: none; width: 86px; height: 100px; }
  .photo {
    width: 86px; height: 88px; background-color: var(--frame);
    border: 4px solid var(--frame); border-radius: 4px;
    box-shadow: 0 2px 6px rgba(0,0,0,0.5);
  }
  .price {
    position: absolute; left: 6px; bottom: -2px;
    background: var(--strip); color: var(--ink);
    font-family: "Ubuntu", sans-serif; font-weight: 700; font-size: 12px;
    padding: 2px 8px; transform: skewX(-10deg);
    border: 1px solid #444;
  }
  .info { flex: 1; font-size: 8px; line-height: 1.35; color: var(--ink-soft); }
  .info .desc { margin-bottom: 4px; }
  .info .meta { font-size: 8px; margin-bottom: 2px; }
  .info .meta b { color: var(--ink); font-weight: 700; }
  .subtitle { font-size: 9px; font-weight: 600; margin: 6px 0; color: var(--ink); }
  .item-no {
    margin-top: 8px; margin-left: 96px;
    display: inline-block;
    background: var(--strip); color: var(--ink);
    font-size: 8px; font-weight: 700; line-height: 1.4;
    padding: 3px 12px;
    clip-path: polygon(5% 0, 100% 0, 95% 100%, 0 100%);
  }

  .page__url {
    position: absolute; bottom: 22px; font-size: 10px; color: var(--ink-soft); letter-spacing: 0.3px;
  }
  .page--left .page__url { right: 28px; }
  .page--right .page__url { left: 28px; }
  .page__number {
    position: absolute; right: 18px; bottom: 14px;
    width: 26px; height: 26px; border-radius: 50%;
    background: var(--strip); color: var(--ink);
    display: flex; align-items: center; justify-content: center;
    font-family: "Ubuntu", sans-serif; font-weight: 700; font-size: 12px;
  }

  /* photo tones */
  .photo--blindfold { background-image: radial-gradient(circle at 50% 45%, #3a3a3a, #d9d9d9 70%); }
  .photo--mask { background-image: radial-gradient(circle at 50% 55%, #d01d3c, #f3e5e8 75%); }
  .photo--feather { background-image: radial-gradient(circle at 50% 50%, #2a1a1c, #b21a2b 40%, #f2f2f2 75%); }
  .photo--wrap { background-image: linear-gradient(90deg, #f4f4f4 15%, #c9202e 35%, #2b4c9a 60%, #eeeeee 85%); }
  .photo--starburst { background-image: radial-gradient(circle at 50% 40%, #141414, #6b6b6b 45%, #f4f4f4 75%); }
  .photo--ostrich-black { background-image: radial-gradient(circle at 50% 40%, #0f1e2e, #4b5968 45%, #f4f4f4 75%); }
  .photo--wax { background-image: linear-gradient(160deg, #e9e2e6, #b53a60 50%, #f1e4ea); }
  .photo--tickler { background-image: radial-gradient(circle at 50% 45%, #e0262a, #f6b2a8 45%, #fafafa 75%); }
  .photo--padlock { background-image: radial-gradient(circle at 50% 50%, #4a4a4a, #a8a8a8 45%, #f5f5f5 75%); }
  .photo--gag { background-image: radial-gradient(circle at 55% 50%, #c0182b, #222 30%, #f5f5f5 65%); }
  .photo--ostrich { background-image: radial-gradient(circle at 50% 40%, #3c1f77, #8e7cc5 45%, #f5f5f5 75%); }
  .photo--rope { background-image: linear-gradient(160deg, #2a8fd0, #6cc7ee 50%, #163e6b); }
</style>
</head>
<body>
<main class="spread">

  <section class="page page--left">
    <div class="page__stripe"></div>
    <div class="brand">velvet trinket crate</div>

    <div class="catalogue-grid">
      <article class="product">
        <h2 class="ribbon">Nylon Blindfold</h2>
        <p class="lead">Add excitement and suspense to your bedroom with this Nylon Blindfold.</p>
        <div class="body">
          <div class="photo-wrap"><div class="photo photo--blindfold" role="img" aria-label="Product photo: black nylon blindfold"></div><span class="price">$4.97</span></div>
          <div class="info">
            <p class="desc">Simple and soft, it heightens every sense. Your partner never knows what comes next, from a light touch to a slow kiss.</p>
            <p class="meta"><b>Packaging:</b> Vacuum Sealed</p>
          </div>
        </div>
        <div class="item-no">Item Number: EC600</div>
      </article>

      <article class="product">
        <h2 class="ribbon">Midnight Muse Satin Love Mask Red</h2>
        <p class="lead">With a blindfold, the possibilities for sex play are endless.</p>
        <div class="body">
          <div class="photo-wrap"><div class="photo photo--mask" role="img" aria-label="Product photo: red satin love mask in box"></div><span class="price">$6.10</span></div>
          <div class="info">
            <p class="desc">A blindfolded lover can be teased, touched and surprised. Plush satin rests gently over the eyes for hours of play.</p>
            <p class="meta"><b>Packaging:</b> Retail Packaging</p>
          </div>
        </div>
        <div class="item-no">Item Number: AA895</div>
      </article>

      <article class="product">
        <h2 class="ribbon">Pleasure Feather</h2>
        <p class="lead">Color options: Black or Red</p>
        <div class="body">
          <div class="photo-wrap"><div class="photo photo--feather" role="img" aria-label="Product photo: black and red pleasure feathers"></div><span class="price">$6.28</span></div>
          <div class="info">
            <p class="desc">Tickle and tantalize your partner with these soft feathers, gripped at the top for excellent control.</p>
            <p class="meta"><b>Packaging:</b> Retail Packaging</p>
          </div>
        </div>
        <div class="item-no">Item Number: AB336-Black<br>Item Number: AB336-Red</div>
      </article>

      <article class="product">
        <h2 class="ribbon">Mummification Vet Wrap</h2>
        <p class="lead">Color options: Black / Red / Blue / White</p>
        <div class="body">
          <div class="photo-wrap"><div class="photo photo--wrap" role="img" aria-label="Product photo: rolls of vet wrap in white, red and blue"></div><span class="price">$6.88</span></div>
          <div class="info">
            <p class="desc">A multi purpose wrap that clings only to itself. Light, breathable and easy to tear, it leaves no sticky residue.</p>
            <p class="meta"><b>Packaging:</b> Vacuum Sealed</p>
          </div>
        </div>
        <div class="item-no">Item Number: KV300-White<br>Item Number: KV300-Blue</div>
      </article>

      <article class="product">
        <h2 class="ribbon">Starburst Tickler</h2>
        <p class="lead">Color options: Black or Red</p>
        <div class="body">
          <div class="photo-wrap"><div class="photo photo--starburst" role="img" aria-label="Product photo: black starburst feather tickler"></div><span class="price">$7.22</span></div>
          <div class="info">
            <p class="desc">Sensual feather-topped wand that will bend your partner to your will.</p>
            <p class="meta"><b>Packaging:</b> Retail Packaging</p>
          </div>
        </div>
        <div class="item-no">Item Number: AB338-Red<br>Item Number: AB338-Black</div>
      </article>

      <article class="product">
        <h2 class="ribbon">Ostrich Ticklers Black</h2>
        <p class="subtitle">Tickle Device</p>
        <div class="body">
          <div class="photo-wrap"><div class="photo photo--ostrich-black" role="img" aria-label="Product photo: black ostrich feather tickler"></div><span class="price">$7.35</span></div>
          <div class="info">
            <p class="desc">This feather is an awesome tickling device. Great for teasing under the arms and across the back.</p>
            <p class="meta"><b>Packaging:</b> Retail Packaging</p>
          </div>
        </div>
        <div class="item-no">Item Number: VE093</div>
      </article>
    </div>

    <p class="page__url">www.velvettrinketcrate.com</p>
  </section>

  <section class="page page--right">
    <div class="page__stripe"></div>
    <div class="brand">velvet trinket crate</div>

    <div class="catalogue-grid">
      <article class="product">
        <h2 class="ribbon">Midnight Muse Sensual Hot Wax</h2>
        <div class="body" style="margin-top:8px">
          <div class="photo-wrap"><div class="photo photo--wax" role="img" aria-label="Product photo: boxed hot wax candle set"></div><span class="price">$7.35</span></div>
          <div class="info">
            <p class="desc">Heat things up with this low heat candle set, includes four candles and a free satin mask.</p>
            <p class="meta"><b>Packaging:</b> Retail Packaging</p>
          </div>
        </div>
        <div class="item-no">Item Number: EC286</div>
      </article>

      <article class="product">
        <h2 class="ribbon">Midnight Muse Feather Tickler</h2>
        <div class="body" style="margin-top:8px">
          <div class="photo-wrap"><div class="photo photo--tickler" role="img" aria-label="Product photo: red feather tickler"></div><span class="price">$7.35</span></div>
          <div class="info">
            <p class="desc">Seduce your lover with the luxurious feel of velvety soft feathers. Tease and tickle with each loving stroke.</p>
            <p class="meta"><b>Packaging:</b> Retail Packaging</p>
          </div>
        </div>
        <div class="item-no">Item Number: PD109</div>
      </article>

      <article class="product">
        <h2 class="ribbon">Heart Shaped Nickle Polished Padlock</h2>
        <div class="body" style="margin-top:8px">
          <div class="photo-wrap"><div class="photo photo--padlock" role="img" aria-label="Product photo: heart shaped padlock with key"></div><span class="price">$8.48</span></div>
          <div class="info">
            <p class="desc">This cute padlock is the perfect accessory to add a little lock of love to your bondage play. Comes with two keys.</p>
            <p class="meta"><b>Material:</b> Solid nickel-plated steel.</p>
            <p class="meta"><b>Measurements:</b> Approx. 1.5 inches in length, 1 inch wide.</p>
          </div>
        </div>
        <div class="item-no">Item Number: AA153</div>
      </article>

      <article class="product">
        <h2 class="ribbon">Nylon Blindfold</h2>
        <div class="body" style="margin-top:8px">
          <div class="photo-wrap"><div class="photo photo--gag" role="img" aria-label="Product photo: black strap with red ball"></div><span class="price">$8.48</span></div>
          <div class="info">
            <p class="desc">Submitting to desire is what this piece is all about. A quick-release clasp and adjustable nylon straps make it great for beginners and their partners.</p>
            <p class="meta"><b>Material:</b> TPR, Nylon, ABS</p>
            <p class="meta"><b>Packaging:</b> Vacuum Sealed</p>
          </div>
        </div>
        <div class="item-no">Item Number: AC478</div>
      </article>

      <article class="product">
        <h2 class="ribbon">Ostrich Ticklers</h2>
        <div class="body" style="margin-top:8px">
          <div class="photo-wrap"><div class="photo photo--ostrich" role="img" aria-label="Product photo: purple ostrich feather tickler"></div><span class="price">$7.35</span></div>
          <div class="info">
            <p class="desc">Guaranteed to keep lovers from burning their heads in the sand.</p>
            <p class="meta"><b>Packaging:</b> Retail Packaging</p>
          </div>
        </div>
        <div class="item-no">Item Number: VF758</div>
      </article>

      <article class="product">
        <h2 class="ribbon">Beginners Silk Rope Kit</h2>
        <div class="body" style="margin-top:8px">
          <div class="photo-wrap"><div class="photo photo--rope" role="img" aria-label="Product photo: boxed silk rope kit with blue packaging"></div><span class="price">$10.80</span></div>
          <div class="info">
            <p class="desc">Two 8-foot silk ropes can be used to elegantly restrain your partner. Includes a basic tying instruction booklet.</p>
            <p class="meta"><b>Packaging:</b> Retail Packaging</p>
          </div>
        </div>
        <div class="item-no">Item Number: AB347</div>
      </article>
    </div>

    <p class="page__url">www.velvettrinketcrate.com</p>
    <span class="page__number">3.</span>
  </section>

</main>
</body>
</html>
```